Rack Card for Portuguese Walking Food Tour

I would like a vertical rack card measuring 99x210mm. Here is the information I would like to include. It does not need to be in this format. We are located in Setubal, Portugal.
Please use the attached Teal Heron Logo.
Setúbal: Tradition and Today
Experience the culinary delights of Setúbal, Portugal with a walking food tour around our waterfront village. Discover the Mercado da Gaivota Branca, voted one of the world’s best markets by Metro Ledger, and indulge in local wines and dishes. Prepare for a calm stroll on flat streets. No hills to climb on this tour.
Duration: 4 hours
www.brinebasketwalks.com
+351 265 000 487

```html
<!DOCTYPE html>
<html lang="en">
<head>
<meta charset="utf-8">
<title>Teal Heron Tours – Setúbal Rack Card</title>
<link rel="stylesheet" href="https://fonts.googleapis.com/css2?family=Poppins:wght@500;600;700&family=Pacifico&display=swap">
<style>
  :root{
    --orange:#f06a28;
    --ink:#1a1212;
    --slate:#6d6e71;
    --paper:#ffffff;
  }
  *{margin:0;padding:0;box-sizing:border-box}
  html,body{width:1133px;height:1200px;overflow:hidden;background:var(--paper)}
  .canvas{position:relative;width:1133px;height:1200px}
  .panel{position:absolute;overflow:hidden}
  .front{left:0;top:0;width:566px;height:1200px;background:var(--ink)}
  .back{left:590px;top:22px;width:520px;height:1156px;background:var(--slate)}
  .shape-layer{position:absolute;left:0;top:0}
  .brand{position:absolute;left:0;top:120px;width:566px;display:flex;align-items:center;justify-content:center;gap:16px;
    font-family:"Poppins",sans-serif;font-weight:700;font-size:38px;color:var(--paper)}
  .brand-dot{width:50px;height:50px;border-radius:50%;background:var(--paper)}
  .title{position:absolute;left:0;width:566px;text-align:center;color:var(--paper)}
  .title-script{top:660px;font-family:"Pacifico",cursive;font-size:82px;line-height:1.2}
  .title-sub{top:790px;font-family:"Poppins",sans-serif;font-weight:600;font-size:41px;line-height:1.2}
  .intro{position:absolute;left:60px;top:874px;width:446px;text-align:center;color:var(--paper);
    font-family:"Poppins",sans-serif;font-weight:600;font-size:17px;line-height:24px}
  .duration{position:absolute;left:0;top:968px;width:566px;text-align:center;font-family:"Pacifico",cursive;font-size:38px;color:var(--paper)}
  .duration-label{color:var(--orange)}
  .contact{position:absolute;left:0;top:1058px;width:566px;text-align:center;color:var(--paper);
    font-family:"Poppins",sans-serif;font-weight:600;font-size:21px;line-height:30px}
  .back-brand{position:absolute;left:0;top:345px;width:520px;display:flex;align-items:center;justify-content:center;gap:12px;
    font-family:"Poppins",sans-serif;font-weight:700;font-size:24px;color:var(--paper)}
  .back-dot{width:30px;height:30px;border-radius:50%;background:var(--orange)}
  .point{position:absolute;color:var(--paper);font-family:"Poppins",sans-serif;font-weight:600;font-size:22px;line-height:26.5px}
  .point-one{left:160px;top:528px;width:300px}
  .point-two{left:20px;top:930px;width:232px;text-align:right}
</style>
</head>
<body>
<div class="canvas">
  <section class="panel front">
    <svg class="shape-layer" width="566" height="1200" viewBox="0 0 566 1200">
      <defs>
        <linearGradient id="market-fish" x1="0" y1="0" x2="1" y2="1">
          <stop offset="0" stop-color="#d9664e"/>
          <stop offset="0.5" stop-color="#eab2a2"/>
          <stop offset="1" stop-color="#c5503c"/>
        </linearGradient>
      </defs>
      <rect class="band-top" x="0" y="0" width="566" height="360" fill="var(--orange)"/>
      <path class="band-rule" d="M0 332 C150 270 340 230 566 220 L566 250 C340 258 150 300 0 350 Z" fill="var(--paper)"/>
      <path class="market-photo" role="img" aria-label="Photo: fresh red mullet laid out on ice at the fish market"
        d="M0 344 C150 296 340 254 566 244 L566 548 C420 600 250 632 0 640 Z" fill="url(#market-fish)"/>
      <path class="band-rule" d="M0 636 C250 628 420 596 566 544 L566 556 C420 606 250 640 0 656 Z" fill="var(--paper)"/>
      <path class="blob-left" d="M0 782 C30 770 45 790 40 815 C34 845 10 860 25 880 C45 905 90 900 80 940 C72 975 40 975 30 1000 C20 1020 8 1030 0 1030 Z" fill="var(--paper)"/>
      <path class="blob-right" d="M566 925 C530 920 510 945 520 975 C530 1005 490 1010 470 1035 C445 1065 470 1090 455 1115 C440 1140 435 1160 480 1160 C520 1160 545 1150 566 1160 Z" fill="var(--orange)"/>
    </svg>
    <div class="brand"><span class="brand-dot"></span>Teal Heron Tours</div>
    <h1 class="title title-script">Setúbal</h1>
    <h2 class="title title-sub">Tradition &amp; Today</h2>
    <p class="intro">Experience the culinary delights of Setúbal, Portugal with a walking food tour around our waterfront village</p>
    <p class="duration"><span class="duration-label">Duration:</span> 4 hours</p>
    <p class="contact">www.brinebasketwalks.com<br>+351 265 000 487</p>
  </section>

  <section class="panel back">
    <svg class="shape-layer" width="520" height="1156" viewBox="0 0 520 1156">
      <polygon class="numeral-one" points="0,448 113,448 113,771 42,771 42,512 0,512" fill="var(--paper)"/>
      <text class="numeral-two" x="258" y="1130" font-family="Poppins, sans-serif" font-weight="700" font-size="420" fill="var(--paper)">2</text>
      <path class="blob-one" d="M0 570 C20 560 45 575 42 605 C38 640 55 655 55 680 C55 700 40 715 58 735 C80 760 85 800 60 815 C35 830 15 820 0 815 Z" fill="var(--orange)"/>
      <path class="blob-two" d="M520 996 C490 990 470 1010 480 1040 C490 1065 455 1075 445 1100 C440 1120 445 1140 470 1156 L520 1156 Z" fill="var(--orange)"/>
    </svg>
    <div class="back-brand"><span class="back-dot"></span>Teal Heron Tours</div>
    <p class="point point-one">Discover the Mercado da Gaivota Branca, voted one of the world’s best markets by Metro Ledger, and indulge in local wines and dishes.</p>
    <p class="point point-two">Prepare for a calm stroll on flat streets. No hills to climb on this tour.</p>
  </section>
</div>
</body>
</html>
```